High end boutique food product label

We are looking for a label design to be used on our range of high end food products. We don't have a design or colour scheme in mind and are interested to see what ideas are submitted.
We would like it to feel sophisticated, chic, and eye-catching.
All of our products are handmade in Australia using Australian ingredients.
The graphics for the label will need to be scaleable to be fit a variety of labels from small squat jars with labels sized 3.5cm high and 7cm wide, to tall thin bottles with labels that are 14cm high and 4.5cm wide.
We would be interested in working with the winning designer to create these different sized labels.
The label submitted for this project should be 14cm high and 4.5cm wide, it should include our logo (file supplied in .jpeg and .ai), the product name 'Extra Virgin Olive Oil' and the size '250ml'.
This is just the front label on a bottle, we are not expecting a rear label to be created currently.
You are welcome to use any fonts you think will look good but the fonts used in our logo are Allaina Medium and Bebas Kai Regular.

```html
<!DOCTYPE html>
<html lang="en">
<head>
<meta charset="UTF-8">
<title>Harlow &amp; Reed — Extra Virgin Olive Oil Label</title>
<link rel="stylesheet" href="https://fonts.googleapis.com/css2?family=Bebas+Neue&family=Raleway:wght@200;400&family=Playfair+Display:wght@600&display=swap">
<style>
  :root {
    --backdrop: #f4f2ed;
    --label-top: #161616;
    --label-bottom: #020202;
    --gold: #b9975b;
    --gold-dim: #5e5236;
    --gold-light: #e0c48a;
    --ink-white: #ffffff;
    --muted: #8e8e8e;
  }
  * { margin: 0; padding: 0; box-sizing: border-box; }
  html, body {
    width: 1200px;
    height: 1116px;
    overflow: hidden;
    background: var(--backdrop);
  }
  .canvas {
    position: relative;
    width: 1200px;
    height: 1116px;
    display: flex;
    align-items: center;
    justify-content: center;
  }
  .label {
    position: relative;
    width: 310px;
    height: 1004px;
    background: linear-gradient(180deg, var(--label-top) 0%, var(--label-bottom) 70%);
    color: var(--ink-white);
    text-align: center;
  }
  .brand {
    position: absolute;
    top: 118px;
    left: 0;
    right: 0;
    display: flex;
    align-items: center;
    justify-content: center;
    gap: 8px;
  }
  .brand-dot {
    width: 9px;
    height: 9px;
    border-radius: 50%;
    background: var(--gold);
  }
  .brand-name {
    font-family: "Playfair Display", serif;
    font-weight: 600;
    font-size: 30px;
    color: var(--ink-white);
    line-height: 1;
  }
  .product-grade {
    position: absolute;
    top: 334px;
    left: 0;
    right: 0;
    font-family: "Raleway", sans-serif;
    font-weight: 200;
    font-size: 25px;
    letter-spacing: 4px;
    color: var(--gold-dim);
  }
  .product-name {
    position: absolute;
    top: 362px;
    left: 0;
    right: 0;
    font-family: "Bebas Neue", sans-serif;
    font-size: 88px;
    line-height: 1;
    letter-spacing: 3px;
    color: var(--ink-white);
  }
  .origin-map {
    position: absolute;
    top: 524px;
    left: 50%;
    width: 52px;
    height: 50px;
    transform: translateX(-50%);
    border-radius: 40% 45% 35% 50%;
    background: linear-gradient(135deg, var(--gold-light), var(--gold));
  }
  .origin-text {
    position: absolute;
    top: 596px;
    left: 0;
    right: 0;
    font-family: "Raleway", sans-serif;
    font-weight: 400;
    font-size: 13px;
    letter-spacing: 2px;
    line-height: 24px;
    color: var(--muted);
  }
  .leaf-art {
    position: absolute;
    left: 6px;
    right: 10px;
    bottom: 0;
    height: 366px;
    background: radial-gradient(ellipse at 50% 65%, rgba(185,151,91,0.35) 0%, rgba(185,151,91,0.12) 45%, rgba(0,0,0,0) 75%);
  }
</style>
</head>
<body>
  <main class="canvas">
    <section class="label">
      <div class="brand">
        <span class="brand-dot"></span>
        <span class="brand-name">Harlow &amp; Reed</span>
      </div>
      <p class="product-grade">EXTRA VIRGIN</p>
      <h1 class="product-name">OLIVE OIL</h1>
      <div class="origin-map" role="img" aria-label="Gold map of Australia"></div>
      <p class="origin-text">HANDMADE IN AUSTRALIA<br>250ML</p>
      <div class="leaf-art" role="img" aria-label="Gold line drawing of olive leaves on a branch"></div>
    </section>
  </main>
</body>
</html>
```